Railvoxa - Train Delay Compensation. We help cummuters in the uk using civic rail get there money

We help train commuter who pay very high price for their rail ticket.on Weekly, Monthly and yearly ticket) get some of their money back when their train is delayed or cancelled up to a max of £300 per month all they need to do is download our app from the app store app or android of visit our website www.railvoxa-example.com . The get back up to 40% the cost of their ticket . No claim no fee!! Unlimited claims !! No form filling , No printing no posting we do all the work just claim and wait for your money through the post.
Task
A6 Size paper design and wordings over the 2 pages front and back . wording should include high impact words like ' Don't be short changed ' ' It's your money get it back!! ' The big deal Get up to 40% of cost of ticket back' ' No claim no fee!' preferable should include on the front page picture of crowd of people packed tight on the train or stuck at a train station. Uk Pictures only please . I have a vector image of the logo of out company if needed will upload a jpeg now

with our app they will get possible claim notifications when their trains is late and they are in line for a compensation which can be between 50% to 100% the cost of a daily ticket

Target Market(s)

train commuter in the uk

Requirements
Must have
• No claim no fee.,The big deal Get up to 40% of cost of ticket back' max of £300 per month. Don't be short changed get it's your money get it back. download out app and we do the rest free trial ! . No filling forms , printing or posting of forms we do all the work for you. Just click claim and wait for your money thorough the post. No claim no fee!! Unlimited claims !! No form filling , No printing no posting we do all the work just claim and wait for your money through the post.
• Logo of the company. Must be high impact and attention grabbing !!
Nice to have
• Pictures of commuters packed in the train. Picture of commuters stranded at the train station because of delayed or cancelled trains.

```html
<!DOCTYPE html>
<html lang="en">
<head>
<meta charset="utf-8">
<title>Railvoxa – Train Delay Compensation Flyer</title>
<link rel="stylesheet" href="https://fonts.googleapis.com/css2?family=Oswald:wght@600;700&family=Mulish:wght@600;700;800&family=Arimo:wght@700&display=swap">
<style>
  :root {
    --navy: #1c2a5e;
    --red: #c8202e;
    --paper: #f3f2f5;
    --stage: #d9d8de;
    --photo-dark: #3a3f52;
    --photo-mid: #6b6e7e;
    --white: #ffffff;
  }
  * { margin: 0; padding: 0; box-sizing: border-box; }
  html, body {
    width: 1041px; height: 1200px; overflow: hidden;
    background: var(--stage);
  }
  .flyer {
    position: absolute; left: 92px; top: 0;
    width: 856px; height: 1200px;
    background: var(--paper);
    overflow: hidden;
    font-family: "Mulish", sans-serif;
    color: var(--navy);
  }
  .headline {
    position: absolute; left: 30px; top: 62px;
    font-family: "Oswald", sans-serif; font-weight: 700;
    font-size: 80px; line-height: 1.1; letter-spacing: -1px;
    text-transform: uppercase;
    transform: rotate(-3deg); transform-origin: left top;
  }
  .headline .line { display: block; }
  .headline .accent { color: var(--red); }
  .shapes { position: absolute; left: 0; top: 0; }
  .badge {
    position: absolute; left: 580px; top: 532px;
    width: 248px; height: 248px; border-radius: 50%;
    background: var(--white);
    border: 10px solid var(--navy);
    box-shadow: inset 0 0 0 7px var(--red), inset 0 0 0 10px var(--white);
    display: flex; flex-direction: column; align-items: center; justify-content: center;
    text-align: center; font-weight: 700; font-size: 29px; line-height: 1.05;
  }
  .badge .red { color: var(--red); }
  .big-deal {
    position: absolute; left: 8px; top: 790px;
    font-weight: 700; font-size: 22px; line-height: 1.25;
    text-transform: uppercase;
    transform: rotate(-5deg); transform-origin: left top;
  }
  .big-deal .red { color: var(--red); }
  .download {
    position: absolute; left: 15px; top: 888px;
    font-family: "Arimo", sans-serif; font-weight: 700; font-size: 26px;
    letter-spacing: -0.5px;
    transform: rotate(-2deg); transform-origin: left top;
  }
  .download .red { color: var(--red); }
  .offer-box {
    position: absolute; left: 24px; top: 930px;
    width: 556px; height: 250px;
    border: 5px solid var(--navy); border-radius: 22px;
    background: var(--paper);
    box-shadow: 7px 7px 0 var(--red);
    transform: rotate(-2deg);
    padding: 26px 18px 0 18px;
    text-transform: uppercase; font-weight: 800;
  }
  .offer-box .trial { font-size: 44px; line-height: 1.1; }
  .offer-box .forms { font-size: 42px; line-height: 1.15; color: var(--red); padding-left: 28px; }
  .offer-box .work { font-size: 28px; line-height: 1.35; margin-top: 8px; }
  .claim-note {
    position: absolute; left: 614px; top: 838px;
    font-weight: 700; font-size: 24px; line-height: 33px;
  }
  .claim-note .red { color: var(--red); }
  .brand {
    position: absolute; left: 590px; top: 1000px; width: 260px;
    text-align: center;
  }
  .brand-mark {
    width: 120px; height: 120px; margin: 0 auto;
    border-radius: 50%; border: 6px solid var(--navy);
  }
  .brand-name {
    margin-top: 8px;
    font-weight: 800; font-size: 32px; letter-spacing: 1px;
    color: var(--red); text-transform: uppercase;
  }
  .brand-tag {
    font-weight: 700; font-size: 12px; letter-spacing: 1.5px;
    color: var(--navy); text-transform: uppercase;
  }
</style>
</head>
<body>
  <main class="flyer">
    <svg class="shapes" width="856" height="1200" viewBox="0 0 856 1200">
      <defs>
        <linearGradient id="photoTone" x1="0" y1="0" x2="1" y2="1">
          <stop offset="0" stop-color="var(--photo-mid)"/>
          <stop offset="1" stop-color="var(--photo-dark)"/>
        </linearGradient>
      </defs>
      <line x1="0" y1="278" x2="856" y2="214" stroke="var(--red)" stroke-width="4" stroke-dasharray="9 5"/>
      <line x1="0" y1="284" x2="856" y2="220" stroke="var(--navy)" stroke-width="3" stroke-dasharray="9 5"/>
      <polygon role="img" aria-label="Photo of commuters packed tightly inside a crowded UK train carriage"
        points="0,291 856,228 856,650 0,745" fill="url(#photoTone)"/>
      <polygon points="0,745 856,650 856,685 0,775" fill="var(--red)"/>
      <line x1="0" y1="874" x2="856" y2="792" stroke="var(--red)" stroke-width="4" stroke-dasharray="9 5"/>
      <line x1="0" y1="880" x2="856" y2="798" stroke="var(--navy)" stroke-width="3" stroke-dasharray="9 5"/>
    </svg>

    <h1 class="headline">
      <span class="line">It's your money</span>
      <span class="line">Get <span class="accent">it back!!</span></span>
    </h1>

    <div class="badge">
      <span class="red">NO<br>CLAIM<br>NO FEE!!</span>
      <span>UNLIMITED<br>CLAIMS!!</span>
    </div>

    <p class="big-deal">The big deal get up to <span class="red">40%</span> of cost of<br>ticket back' max of <span class="red">£300 per month</span>.</p>

    <p class="download"><span class="red">Download Our App</span> And We Do The Rest</p>

    <section class="offer-box">
      <p class="trial">Free trial !</p>
      <p class="forms">No filling forms !</p>
      <p class="work">Printing or posting of forms<br>we do all the work for you.</p>
    </section>

    <p class="claim-note">Just <span class="red">click claim</span><br>and wait for your<br>money through<br>the post.</p>

    <div class="brand">
      <div class="brand-mark"></div>
      <p class="brand-name">Railvoxa</p>
      <p class="brand-tag">Train delay compensation</p>
    </div>
  </main>
</body>
</html>
```